LOS PINOS DE ARENA - EXCLUSIVE AND LUXURY REAL ESTATE PROJECT

Se trata del diseño de un mono poste grande (4 m x 2 m) o (8m x 3m) anunciando la construcción de 30 villas de lujo en un terreno en primera línea de playa en el sur de España (Cádiz).

La idea es crear expectación y transmitir lujo y exclusividad.

Target Market(s)

Clientes de alto poder adquisitivo que quieran adquirir su segunda vivienda en un entorno privilegiado a escasos pasos de una de las playas más bonitas de Cádiz.

Industry/Entity Type

REAL ESTATE

Colors

Designer to choose colors to be used in the design.

Requirements
Must have
• LOS PINOS DE ARENA as the name of the development
Nice to have
• Crear expectación con ideas del tipo: “Coming soon” o “No te lo puedes perder”

```html
<!DOCTYPE html>
<html lang="es">
<head>
<meta charset="utf-8">
<title>Los Pinos de Arena – Valla publicitaria</title>
<link href="https://fonts.googleapis.com/css2?family=Cinzel:wght@400&family=Montserrat:wght@600;700;800&display=swap" rel="stylesheet">
<style>
  :root {
    --page-bg: #cfcfcf;
    --navy: #232a96;
    --navy-deep: #1b2185;
    --orange: #ff6a00;
    --orange-red: #e8393a;
    --white: #ffffff;
    --sky: #5f8fd6;
    --sand: #e9e4da;
  }
  html, body {
    margin: 0;
    padding: 0;
    width: 1171px;
    height: 1200px;
    overflow: hidden;
    background: var(--page-bg);
  }
  .billboard {
    position: absolute;
    left: 11px;
    top: 385px;
    width: 1148px;
    height: 430px;
    overflow: hidden;
    box-shadow: 18px 18px 14px rgba(0,0,0,0.35);
    font-family: "Montserrat", sans-serif;
    color: var(--white);
  }
  .billboard__shapes {
    position: absolute;
    inset: 0;
  }
  .billboard__copy {
    position: absolute;
    left: 654px;
    top: 0;
    width: 400px;
    text-align: center;
  }
  .title {
    margin: 26px 0 0;
    font-family: "Cinzel", serif;
    font-weight: 400;
    font-size: 54px;
    line-height: 60px;
    letter-spacing: 1px;
  }
  .tagline {
    margin: 10px 0 0;
    font-weight: 600;
    font-size: 15.5px;
    line-height: 23px;
  }
  .cta-pill {
    display: inline-block;
    margin-top: 16px;
    padding: 6px 18px 8px;
    border-radius: 6px 6px 12px 6px;
    background: linear-gradient(90deg, var(--orange-red), var(--orange));
    font-weight: 800;
    font-size: 27px;
    line-height: 30px;
  }
  .pitch {
    margin: 14px 0 0;
    font-weight: 600;
    font-size: 15.5px;
    line-height: 22px;
  }
  .divider {
    position: relative;
    height: 1px;
    margin: 12px 10px 0;
    background: rgba(255,255,255,0.85);
  }
  .divider::after {
    content: "";
    position: absolute;
    left: 50%;
    top: -1px;
    width: 52px;
    height: 3px;
    transform: translateX(-50%);
    background: var(--orange-red);
  }
  .call {
    margin: 12px 0 0;
    font-weight: 800;
    font-size: 24px;
    line-height: 30px;
  }
</style>
</head>
<body>
  <section class="billboard">
    <svg class="billboard__shapes" width="1148" height="430" viewBox="0 0 1148 430">
      <defs>
        <linearGradient id="orangeField" x1="0" y1="0" x2="0.4" y2="1">
          <stop offset="0" stop-color="#ff6a00"/>
          <stop offset="1" stop-color="#e8393a"/>
        </linearGradient>
        <linearGradient id="photoTone" x1="0" y1="0" x2="0" y2="1">
          <stop offset="0" stop-color="#5f8fd6"/>
          <stop offset="0.45" stop-color="#c9cfd6"/>
          <stop offset="1" stop-color="#e9e4da"/>
        </linearGradient>
      </defs>
      <rect class="field-orange" width="1148" height="430" fill="url(#orangeField)"/>
      <path class="field-navy" d="M400 0 H1148 V230 C1148 350 1090 430 990 430 H280 V300 C280 100 330 0 400 0 Z" fill="#232a96"/>
      <path class="photo" role="img" aria-label="Render de una villa moderna blanca con terraza, piscina y cielo azul"
            d="M29 29 H461 Q561 29 561 129 V400 H139 Q29 400 29 290 Z" fill="url(#photoTone)"/>
    </svg>

    <div class="billboard__copy">
      <h1 class="title">LOS PINOS<br>DE ARENA</h1>
      <p class="tagline">30 villas de lujo en un terreno en primera línea<br>de playa en el sur de España (Cádiz).</p>
      <div class="cta-pill">No te lo puedes perder</div>
      <p class="pitch">Compra tu segunda vivienda en un entorno<br>privilegiado a unos pasos de una de las playas<br>más bonitas de Cádiz.</p>
      <div class="divider"></div>
      <p class="call">Llámenos hoy: 4512 306 778</p>
    </div>
  </section>
</body>
</html>
```